(Expedite)Project GoldenHarvest:Website home page template design for not-for-profit organization.
Change Starts With You!
(Expedite)Project GoldenHarvest:Website home page template design for not-for-profit organization. - Fund Raising
Creative Brief
Fund Raising
https://goldenharvestcare.org/
Project Golden Harvest is a not-for-profit organization driven by law enforcement officials and retired PGL players, who are committed to providing Christmas gifts for families in need.
“We only need the template design in a layered PSD file – no HTML code is needed.” The most important characteristic is incorporating a subtle holiday theme similar to the Hidden Gifter! site located at http://hiddengifter.com/.
Friendly
For Children
below header
http://hiddengifter.com/
http://www.giftsforkidsinneed.org/
https://www.commonhelpfund.org/
The client is looking to make the current draft site found at https://goldenharvestcare.org/ more holiday oriented. Background images and buttons as well as the menubar need a subtle holiday accent. They particularly like the banner photo used on the Gifts for Kids website found at http://www.giftsforkidsinneed.org/. Like Gifts for Kids, this organization is driven by people in uniforms and, while it is not necessary, they are hoping to incorporate their uniforms in the banner photo. Also like Gifts for Kids and the Common Help website found at https://www.commonhelpfund.org/, they will have some high-profile corporate sponsors. The page width is set at a maximum of 940 pixels and the banner dimensions are 670x250.

```html
<!DOCTYPE html>
<html lang="en">
<head>
<meta charset="utf-8">
<title>Project Golden Harvest – Home</title>
<link rel="stylesheet" href="https://fonts.googleapis.com/css2?family=Questrial&family=Montserrat:wght@600;700&display=swap">
<style>
:root{
  --red:#d71920;
  --red-dark:#a50f14;
  --navy:#1d2a5c;
  --blue:#1e3f9a;
  --ink:#333333;
  --muted:#7a7a7a;
  --line:#dcdcdc;
  --panel:#f4f4f4;
  --white:#ffffff;
  --snow:#f3e9e9;
}
*{box-sizing:border-box;margin:0;padding:0}
html,body{width:1200px;height:914px;overflow:hidden}
body{position:relative;background:var(--white);font-family:"Questrial",sans-serif;color:var(--ink)}
.side-decor{position:absolute;top:0;width:174px;height:868px;background:linear-gradient(180deg,#fbf4f4,#f1e2e2 50%,#f8efef)}
.side-decor.left{left:0}
.side-decor.right{right:0;width:94px}
.page{position:absolute;left:174px;top:0;width:932px;height:868px;background:var(--white);box-shadow:0 0 18px rgba(0,0,0,.12)}
.topbar{position:absolute;left:0;top:0;width:100%;height:40px}
.search{position:absolute;left:16px;top:8px;width:270px;height:24px;border:1px solid var(--line);border-radius:12px;font-size:12px;color:var(--muted);padding:4px 12px}
.search svg{position:absolute;right:10px;top:5px}
.cta-pill{position:absolute;right:16px;top:2px;height:30px;padding:0 16px 0 40px;background:var(--navy);color:var(--white);border-radius:15px;font-size:13px;line-height:30px}
.cta-pill b{font-family:"Montserrat",sans-serif;font-weight:700}
.cta-pill .dot{position:absolute;left:8px;top:5px;width:20px;height:20px;border-radius:50%;background:var(--white)}
.drape{position:absolute;left:0;top:60px;width:100%;height:120px;background:linear-gradient(180deg,var(--red-dark),var(--red) 40%,rgba(232,68,74,.45) 75%,rgba(255,255,255,0))}
.nav{position:absolute;top:60px;height:36px;display:flex;gap:28px;align-items:center;font-family:"Montserrat",sans-serif;font-weight:700;font-size:12px;color:var(--white)}
.nav.left{left:20px}
.nav.right{right:20px}
.nav .active{color:var(--red);background:var(--white);padding:4px 8px;border-radius:3px}
.brand{position:absolute;left:346px;top:44px;width:200px;height:130px;display:flex;flex-direction:column;align-items:center;justify-content:center;gap:8px;background:var(--white);border-radius:20px;box-shadow:0 2px 10px rgba(0,0,0,.2)}
.brand .mark{width:34px;height:34px;border-radius:50%;background:var(--blue)}
.brand .name{font-size:20px;color:var(--blue);text-align:center;line-height:1.1}
.art{position:absolute;border-radius:10px}
.art.baubles{left:8px;top:100px;width:140px;height:110px;background:radial-gradient(ellipse at 50% 45%,rgba(200,16,46,.55),rgba(240,200,200,.25) 70%,rgba(255,255,255,0))}
.art.tree-top{left:578px;top:100px;width:96px;height:110px;background:radial-gradient(ellipse at 50% 60%,rgba(47,125,50,.55),rgba(200,230,200,.2) 70%,rgba(255,255,255,0))}
.art.tree-left{left:0;top:410px;width:116px;height:122px;background:radial-gradient(ellipse at 50% 60%,rgba(47,125,50,.5),rgba(220,235,220,.2) 70%,rgba(255,255,255,0))}
.art.santa{left:752px;top:300px;width:120px;height:200px;background:radial-gradient(ellipse at 50% 50%,rgba(200,16,46,.55),rgba(245,225,225,.3) 70%,rgba(255,255,255,0))}
.art.footer-tree{left:14px;top:8px;width:80px;height:96px;background:radial-gradient(ellipse at 50% 55%,rgba(215,25,32,.55),rgba(250,220,220,.25) 70%,rgba(255,255,255,0))}
.tagline-top{position:absolute;left:0;top:222px;width:100%;text-align:center;font-size:20px;color:var(--navy)}
.tagline-top b{font-family:"Montserrat",sans-serif;font-weight:700;color:var(--blue);font-size:24px}
.banner{position:absolute;left:119px;top:272px;width:409px;height:240px;background:linear-gradient(180deg,#0f1f45,#2c3c63 55%,#7a6a4a);border-radius:4px}
.banner-dots{position:absolute;left:119px;top:496px;width:409px;display:flex;justify-content:center;gap:8px}
.banner-dots span{width:8px;height:8px;border-radius:50%;background:rgba(255,255,255,.6)}
.banner-dots span:first-child{background:var(--red)}
.help-panel{position:absolute;left:528px;top:272px;width:220px;height:240px;background:var(--white);border:1px solid var(--line);border-left:none;padding:14px 16px}
.help-panel h3{font-family:"Montserrat",sans-serif;font-weight:700;font-size:19px;color:var(--red);line-height:1.1}
.help-panel .lead{font-size:14px;color:var(--navy);margin:4px 0 16px;line-height:1.3}
.help-panel .small{font-size:11px;color:var(--muted);margin:4px 0 16px}
.cause-strip{position:absolute;left:0;top:540px;width:100%;height:34px;background:linear-gradient(180deg,#f7f7f7,#e9e9e9);text-align:center;line-height:34px;font-size:14px;color:var(--ink)}
.cause-strip .blue{color:var(--blue);font-weight:700}
.cause-strip .red{color:var(--red);font-weight:700}
.cause-strip .navy{color:var(--navy);font-weight:700}
.steps{position:absolute;left:0;top:596px;width:100%;height:150px;background:var(--panel)}
.step{position:absolute;top:10px;width:286px;height:132px;background:var(--white);border:1px solid var(--line);border-radius:6px;box-shadow:0 2px 6px rgba(0,0,0,.1);padding:14px}
.step .num{position:absolute;left:14px;top:14px;width:48px;height:48px;border-radius:4px;color:var(--white);font-family:"Montserrat",sans-serif;font-weight:700;font-size:26px;text-align:center;line-height:48px}
.step .num.red{background:var(--red)}
.step .num.dark{background:#444}
.step h4{margin-left:58px;font-family:"Montserrat",sans-serif;font-weight:600;font-size:16px;color:var(--ink)}
.step .sub{margin-left:58px;font-size:12px;color:var(--red);margin-top:2px}
.step p{margin-left:58px;margin-top:10px;font-size:10px;color:var(--muted);line-height:1.4}
.step .arrow{position:absolute;right:-16px;top:50px}
.footer{position:absolute;left:0;top:752px;width:100%;height:116px}
.contact{position:absolute;left:110px;top:48px;font-size:12px;line-height:1.6}
.contact .label{color:var(--red)}
.social{position:absolute;left:560px;top:74px;display:flex;gap:4px}
.social span{width:26px;height:26px;border-radius:4px;background:var(--blue)}
.social span:nth-child(2){background:#4fa3d9}
.social span:nth-child(3){background:#f08a24}
.footer-brand{position:absolute;right:120px;top:22px;width:150px;height:90px;background:var(--white);border-radius:16px;box-shadow:0 2px 8px rgba(0,0,0,.2);display:flex;align-items:center;justify-content:center;gap:8px;padding:8px}
.footer-brand .mark{width:20px;height:20px;border-radius:50%;background:var(--blue);flex:none}
.footer-brand .name{font-size:14px;color:var(--blue);line-height:1.1}
.legal{position:absolute;left:0;top:868px;width:1200px;height:46px;background:var(--red);color:var(--white);font-size:11px;padding:8px 0 0 190px;line-height:1.5}
</style>
</head>
<body>
<div class="side-decor left" role="img" aria-label="Soft snowflake pattern with hanging Christmas ornaments"></div>
<div class="side-decor right" role="img" aria-label="Soft snowflake pattern with hanging Christmas ornaments"></div>

<div class="page">
  <div class="topbar">
    <div class="search">Search ...
      <svg width="14" height="14" viewBox="0 0 14 14"><circle cx="6" cy="6" r="4.5" fill="none" stroke="#999" stroke-width="1.5"/><line x1="9.5" y1="9.5" x2="13" y2="13" stroke="#999" stroke-width="1.5"/></svg>
    </div>
    <div class="cta-pill"><span class="dot"></span>Learn how you can <b>Make A Difference</b></div>
  </div>

  <div class="drape" role="img" aria-label="Red holiday curtain drape behind the menu"></div>
  <div class="art baubles" role="img" aria-label="Hanging red and gold Christmas baubles"></div>
  <div class="art tree-top" role="img" aria-label="Decorated Christmas tree"></div>

  <nav class="nav left"><span class="active">HOME</span><span>ABOUT</span><span>FAQ</span><span>CONTACT</span></nav>
  <nav class="nav right"><span>OUR WORK</span><span>DONATE</span><span>CORPORATE SPONSORS</span></nav>

  <div class="brand"><span class="mark"></span><span class="name">Project Golden Harvest</span></div>

  <div class="tagline-top">Change Starts with <b>You</b>!</div>

  <div class="art tree-left" role="img" aria-label="Snowy Christmas tree illustration"></div>
  <div class="banner" role="img" aria-label="Banner illustration of Santa's sleigh flying over a snowy night"></div>
  <div class="banner-dots"><span></span><span></span><span></span><span></span></div>

  <aside class="help-panel">
    <h3>HELP</h3>
    <p class="lead">Make A Difference in Childern Life!</p>
    <h3>DONATE</h3>
    <p class="small">Make a tax-deductible donation</p>
    <h3>REQUEST HELP</h3>
    <p class="small">Get help for a family need in</p>
  </aside>
  <div class="art santa" role="img" aria-label="Santa Claus illustration"></div>

  <div class="cause-strip">Be a part of <span class="blue">Project Golden Harvest</span> and help us <span class="red">Make a Difference</span> in the lives of <span class="navy">deserving families.</span></div>

  <section class="steps">
    <article class="step" style="left:14px">
      <span class="num red">01</span>
      <h4>Make A Donation!</h4>
      <div class="sub">Make A Difference</div>
      <p>Your gift brings warmth and hope to a local family this season. Every dollar helps us reach one more home.</p>
      <svg class="arrow" width="10" height="14" viewBox="0 0 10 14"><path d="M1 1l7 6-7 6z" fill="#c8102e"/></svg>
    </article>
    <article class="step" style="left:322px">
      <span class="num dark">02</span>
      <h4>Spread The Word</h4>
      <div class="sub">Make A Difference</div>
      <p>Tell friends and neighbors about our mission. Share our story online and help more families find the support they need.</p>
      <svg class="arrow" width="10" height="14" viewBox="0 0 10 14"><path d="M1 1l7 6-7 6z" fill="#c8102e"/></svg>
    </article>
    <article class="step" style="left:630px">
      <span class="num dark">03</span>
      <h4>Become A Volunteer</h4>
      <div class="sub">Make A Difference</div>
      <p>Give a few hours of your time to sort, wrap and deliver gifts to children across our community this winter.</p>
    </article>
  </section>

  <footer class="footer">
    <div class="art footer-tree" role="img" aria-label="Red Christmas tree illustration"></div>
    <div class="contact">
      <div><span class="label">Email:</span> info@projectgoldenharvest.com</div>
      <div><span class="label">Cell:</span> +00 5555555 555</div>
    </div>
    <div class="social"><span></span><span></span><span></span></div>
    <div class="footer-brand"><span class="mark"></span><span class="name">Project Golden Harvest</span></div>
  </footer>
</div>

<div class="legal">Project Golden Harvest is a 501c3 organization, 2012 © All Rights Reserved.<br>Terms of Use | Privacy Policy</div>
</body>
</html>
```